Tito - Idiomas Corvalo

2x Design Concepts for the home page and interior pages based on the attached brief and powerpoint presentation.

Colours: see 2.1 logo and heading for logo colours and website colours

Home Page: (please see attached file)
1)Logo to appear in the top left, heading to include telephone numbers and a best price (credibility stamp) - see 2.1
2)the toolbar is to be centered at the top. Emphasis must be placed on the 5 easy steps to study english in Australia - see 2.2
3) modules. 5x modules required in the home page for: home page image rotator, online quote tool, enquiry form, best deals, quick links (there are 2 examples for the quick links module - open to suggestions) - see 2.3
4) footer. the footer is to include partner logos with hyperlinks to the partner websites. with a copywright section at the base - see 2.4
5) 2.5 is the basic idea - open to design suggestions. The website objective is to submit an online quote or contact Idiomas Corvalo.

Internal Page: - see 3-
open to all suggestion. Require a lot of space for internal custom design concepts (these are taking place inhouse). The interior page must have a side module toolbar to include:
1) a modified online quote tool
2) modified enquiry form
3) modified quick links section

Target Market(s)

target market is young (17-30yrs) Brazilians looking to study English in Australia or continue studying English in Australia that can also acquire visa sponsorship.

The buyer will be the parents of the students. the design must appeal to both markets.

Number of Pages Required

2 pages

Requirements
Must have
• see project overview
2x design concepts for the home page and interior page
professional, clean, simple and easy to navigate

```html
<!DOCTYPE html>
<html lang="en">
<head>
<meta charset="utf-8">
<title>Idiomas Corvalo – Home and Interior Page Concepts</title>
<link href="https://fonts.googleapis.com/css2?family=Arimo:wght@400;700&display=swap" rel="stylesheet">
<style>
:root{
  --green-dark:#2b6449;
  --green:#3d7a5b;
  --green-light:#5f9a78;
  --blue-dark:#1d4f8f;
  --blue:#2d64a6;
  --blue-light:#7ea3c9;
  --panel:#e8ecea;
  --rule:#d8dcda;
  --text:#222;
  --muted:#7a7f7d;
  --teal:#2b6a52;
  --orange:#ec9043;
  --orange-light:#f6b87c;
  --gold:#e0a515;
  --navy:#2a3f7d;
  --yellow:#f5d94a;
}
*{box-sizing:border-box;margin:0;padding:0}
html,body{width:1200px;height:994px;overflow:hidden;background:#fff}
body{position:relative;font-family:"Arimo",Arial,sans-serif;color:var(--text)}
.page{position:absolute;background:#fff;box-shadow:0 0 6px rgba(0,0,0,.28);overflow:hidden}
.page--home{left:9px;top:9px;width:843px;height:772px;z-index:2}
.page--interior{left:344px;top:208px;width:845px;height:777px;z-index:1}
.abs{position:absolute}

/* header */
.brand{left:84px;top:32px;font-size:22px;font-weight:700;color:var(--green-dark);letter-spacing:-.3px}
.phones{font-size:14px;font-weight:700;color:#555;line-height:26px}
.phones li{list-style:none;display:flex;align-items:center;gap:6px}
.flag{width:27px;height:16px;border-radius:2px;display:inline-block}
.flag--au{background:var(--blue-dark)}
.flag--br{background:#2f9a45}
.price-badge{width:78px;height:78px;border-radius:50%;background:var(--gold)}

/* nav */
.nav{display:flex;height:27px;border-radius:2px;overflow:hidden;font-size:13px}
.nav a{display:flex;align-items:center;justify-content:center;color:#fff;text-decoration:none;border-right:1px solid rgba(255,255,255,.25);gap:4px}
.nav .g{background:linear-gradient(var(--green-light),var(--green-dark))}
.nav .b{background:linear-gradient(#3b74b8,var(--blue-dark))}
.nav .l{background:linear-gradient(#9dbbd9,var(--blue-light))}
.nav .on{color:var(--yellow)}
.caret{font-size:8px}

/* hero & quote */
.hero{left:77px;top:137px;width:373px;height:247px;background:linear-gradient(120deg,#f3e6cf 0%,#d9c7a8 35%,#b9cfe0 70%,#e8eef3 100%)}
.quote{left:456px;top:137px;width:308px;height:247px;background:var(--green-dark);color:#fff;border-radius:2px}
.quote h2{position:absolute;left:22px;top:16px;font-size:18px}
.quote h3{font-weight:400;font-size:14px}
.cities{list-style:none;font-size:11px;line-height:13px;margin:8px 0 0 10px}
.cities li{display:flex;align-items:center;gap:6px}
.cities li::before{content:"";width:7px;height:7px;border-radius:50%;background:#fff}
.field{background:#fff;border:1px solid #bbb;height:16px}
.btn{display:flex;align-items:center;justify-content:center;color:#fff;background:linear-gradient(var(--orange-light),var(--orange));border:1px solid #d07a30;border-radius:4px;font-size:14px}

/* lower modules */
.title{font-size:18px;font-weight:700;color:var(--teal)}
.vrule{width:1px;background:var(--rule)}
.deals{list-style:none}
.deals li{display:flex;align-items:center;gap:12px;height:30px;border-bottom:1px solid var(--rule);font-size:11px}
.tag{position:relative;width:62px;height:23px;background:linear-gradient(var(--green-light),var(--green-dark));color:#fff;font-size:10px;font-weight:700;display:flex;align-items:center;justify-content:center}
.tag::after{content:"";position:absolute;right:-6px;top:7px;border-left:6px solid var(--green-dark);border-top:5px solid transparent;border-bottom:5px solid transparent}
.more{font-size:10px;color:var(--teal)}
.ask{background:var(--panel);border-radius:3px;font-size:11px}
.ask label{position:absolute;left:10px}
.ask .field{position:absolute;border:none}
.link-item .thumb{position:absolute;left:0;top:0;width:54px;height:54px;background:var(--panel);border-radius:3px}
.link-item h4{position:absolute;left:66px;top:0;font-size:11px}
.link-item p{position:absolute;left:66px;top:14px;width:176px;font-size:9.5px;line-height:11px}
.link-item .more{position:absolute;right:0;top:48px}

/* footer */
.footer{height:52px;background:#e6e9e8;font-size:9.5px;color:var(--muted)}
.footer p{position:absolute;left:16px;line-height:14px}
.pay-badge{width:62px;height:24px;background:var(--navy);border-radius:4px}
.partner{font-size:22px;font-weight:700;color:var(--navy)}

/* interior sidebar */
.side-head{height:20px;background:linear-gradient(var(--green-light),var(--green-dark));color:#fff;font-size:13px;font-weight:700;padding-left:7px;display:flex;align-items:center;border-radius:2px 2px 0 0}
.side-panel{background:var(--panel);color:var(--teal)}
.side-panel .cities{color:#333;margin:4px 0 0 16px}
.side-panel .cities li::before{background:#fff;border:1px solid #666}
.side-links{list-style:none;font-size:10px;color:var(--orange);line-height:12.5px}
</style>
</head>
<body>

<!-- interior page (behind) -->
<section class="page page--interior" aria-label="Interior page concept">
  <ul class="phones abs" style="left:556px;top:16px">
    <li><span class="flag flag--au"></span>0 800 555 010</li>
    <li><span class="flag flag--br"></span>1 800 555 020</li>
  </ul>
  <div class="price-badge abs" style="left:685px;top:8px" role="img" aria-label="Best price guarantee badge"></div>
  <nav class="nav abs" style="left:77px;top:99px;width:692px">
    <a class="g on" style="width:65px">Home</a><a class="g" style="width:92px">Promotions</a><a class="b" style="width:85px">Schools <span class="caret">▼</span></a><a class="b" style="width:73px">Cities <span class="caret">▼</span></a><a class="l" style="width:84px">Air Tickets</a><a class="l" style="width:59px">Visa</a><a class="l" style="width:97px">Final Details</a><a class="g" style="width:77px">Contact</a><a class="g" style="width:60px">Blog</a>
  </nav>

  <aside class="abs" style="left:622px;top:140px;width:147px">
    <div class="side-head">› ONLINE QUOTE</div>
    <div class="side-panel" style="height:224px;padding:10px 12px 0;position:relative">
      <h3 style="font-size:13px;font-weight:400">Choose your city</h3>
      <ul class="cities"><li>Sydney</li><li>Melbourne</li><li>Gold Coast</li><li>Brisbane</li><li>Perth</li><li>Adelaide</li><li>Byron Bay</li></ul>
      <h3 style="font-size:13px;font-weight:400;margin-top:12px">Duration</h3>
      <div class="field" style="width:104px;margin-top:4px;border-color:#666"></div>
      <div class="btn abs" style="left:12px;top:180px;width:120px;height:32px;font-size:11px">GET A QUOTE NOW</div>
    </div>

    <div class="side-head" style="margin-top:14px">ASK US QUESTIONS</div>
    <div class="side-panel" style="height:215px;position:relative;font-size:11px">
      <p class="abs" style="left:7px;top:6px">Please ask us a question.</p>
      <p class="abs" style="left:8px;top:30px;color:#222">Name:</p><div class="field abs" style="left:43px;top:28px;width:100px;border:none"></div>
      <p class="abs" style="left:8px;top:53px;color:#222">Email:</p><div class="field abs" style="left:43px;top:51px;width:100px;border:none"></div>
      <p class="abs" style="left:8px;top:76px;color:#222">Phone:</p><div class="field abs" style="left:43px;top:74px;width:100px;border:none"></div>
      <p class="abs" style="left:8px;top:99px;color:#222">Question:</p><div class="field abs" style="left:10px;top:115px;width:133px;height:54px;border:none"></div>
      <div class="btn abs" style="left:15px;top:180px;width:116px;height:25px;font-size:11px">SEND</div>
    </div>

    <div style="border-top:1px solid var(--rule);margin-top:10px;padding-top:7px">
      <h2 class="title" style="font-size:13px">QUICK LINKS</h2>
      <ul class="side-links" style="margin-top:3px">
        <li>▸ Promotions</li><li>▸ Advantage</li><li>▸ Payment Option</li><li>▸ Accommodation</li>
      </ul>
    </div>
  </aside>

  <footer class="footer abs" style="left:78px;top:723px;width:691px">
    <p style="top:12px">© 2010 Idiomas Corvalo. All rights reserved.<br>Privacy Policy &nbsp;|&nbsp; Terms and Conditions &nbsp;|&nbsp; FAQ &nbsp;|&nbsp; Contact Us</p>
    <div class="pay-badge abs" style="left:498px;top:14px"></div>
    <div class="partner abs" style="left:590px;top:12px">Pagora</div>
  </footer>
</section>

<!-- home page (front) -->
<section class="page page--home" aria-label="Home page concept">
  <div class="brand abs">Idiomas Corvalo</div>
  <ul class="phones abs" style="left:555px;top:25px">
    <li><span class="flag flag--au"></span>0 800 555 010</li>
    <li><span class="flag flag--br"></span>1 800 555 020</li>
  </ul>
  <div class="price-badge abs" style="left:681px;top:8px" role="img" aria-label="Best price guarantee badge"></div>

  <nav class="nav abs" style="left:77px;top:97px;width:688px">
    <a class="g on" style="width:65px">Home</a><a class="g" style="width:92px">Promotions</a><a class="b" style="width:85px">Schools <span class="caret">▼</span></a><a class="b" style="width:73px">Cities <span class="caret">▼</span></a><a class="l" style="width:84px">Air Tickets</a><a class="l" style="width:59px">Visa</a><a class="l" style="width:97px">Final Details</a><a class="g" style="width:77px">Contact</a><a class="g" style="width:56px">Blog</a>
  </nav>

  <div class="hero abs" role="img" aria-label="Photo of smiling young students studying together at a desk"></div>

  <div class="quote abs">
    <h2>› ONLINE QUOTE</h2>
    <div class="abs" style="left:40px;top:58px">
      <h3>Choose your city</h3>
      <ul class="cities"><li>Sydney</li><li>Melbourne</li><li>Gold Coast</li><li>Brisbane</li><li>Perth</li><li>Adelaide</li><li>Byron Bay</li></ul>
    </div>
    <div class="abs" style="left:190px;top:58px">
      <h3>Duration</h3>
      <div class="field" style="width:88px;margin-top:7px"></div>
    </div>
    <div class="btn abs" style="left:50px;top:194px;width:204px;height:37px">GET A QUOTE NOW</div>
  </div>

  <!-- best deals -->
  <div class="abs" style="left:75px;top:401px;width:213px">
    <h2 class="title">BEST DEALS</h2>
    <ul class="deals" style="margin-top:9px">
      <li><span class="tag">Sydney</span>2 Semesters for $6,000*</li>
      <li><span class="tag">Melbourne</span>2 Semesters for $6,000*</li>
      <li><span class="tag">Gold Coast</span>2 Semesters for $6,000*</li>
      <li><span class="tag">Brisbane</span>2 Semesters for $6,000*</li>
      <li><span class="tag">Perth</span>2 Semesters for $6,000*</li>
      <li><span class="tag">Adelaide</span>2 Semesters for $6,000*</li>
      <li><span class="tag">Byron Bay</span>2 Semesters for $6,000*</li>
    </ul>
    <p class="more" style="text-align:right;margin-top:9px">Find out more ▸</p>
  </div>
  <div class="vrule abs" style="left:304px;top:404px;height:278px"></div>

  <!-- ask us -->
  <div class="abs" style="left:312px;top:401px;width:199px">
    <h2 class="title">ASK US QUESTIONS</h2>
    <div class="ask abs" style="left:0;top:31px;width:188px;height:233px">
      <p class="abs" style="left:10px;top:18px">Please ask us a question.</p>
      <label style="top:47px">Name:</label><div class="field" style="left:49px;top:45px;width:127px"></div>
      <label style="top:70px">Email:</label><div class="field" style="left:49px;top:68px;width:127px"></div>
      <label style="top:93px">Phone:</label><div class="field" style="left:49px;top:91px;width:127px"></div>
      <label style="top:116px">Question:</label><div class="field" style="left:61px;top:115px;width:115px;height:61px"></div>
      <div class="btn abs" style="left:39px;top:192px;width:116px;height:27px">SEND</div>
    </div>
  </div>
  <div class="vrule abs" style="left:509px;top:404px;height:278px"></div>

  <!-- quick links -->
  <div class="abs" style="left:518px;top:401px;width:243px;height:300px">
    <h2 class="title">QUICK LINKS</h2>
    <div class="link-item abs" style="left:0;top:33px;width:243px;height:60px">
      <div class="thumb"></div><h4>Promotions</h4>
      <p>Promotions promotionspromotions promoti promotionsprom promotions.</p>
      <span class="more">Find out more ▸</span>
    </div>
    <div class="link-item abs" style="left:0;top:124px;width:243px;height:60px">
      <div class="thumb"></div><h4>Advantages</h4>
      <p>Promotions promotionspromotions promoti promotionsprom promotions.</p>
      <span class="more">Find out more ▸</span>
    </div>
    <div class="link-item abs" style="left:0;top:217px;width:243px;height:60px">
      <div class="thumb"></div><h4>Payment Option</h4>
      <p>Promotions promotionspromotions promoti promotionsprom promotions.</p>
      <span class="more">Find out more ▸</span>
    </div>
  </div>

  <footer class="footer abs" style="left:77px;top:721px;width:688px">
    <p style="top:12px">© 2010 Idiomas Corvalo. All rights reserved.<br>Privacy Policy &nbsp;|&nbsp; Terms and Conditions &nbsp;|&nbsp; FAQ &nbsp;|&nbsp; Contact Us</p>
    <div class="pay-badge abs" style="left:494px;top:14px"></div>
    <div class="partner abs" style="left:590px;top:12px">Pagora</div>
  </footer>
</section>

</body>
</html>
```